Professional Personal Website with Blog and four sections

I am seeking a website design for myself. I would like the site to contain a blog, related to Information Security and several sections.

I am an established Information Security Consultant (one aspect of the site).
I am an author of a children's spiritual book that is "new thought" (another aspect of the site)
I am a co-founder of a secure social platform for kids and families (www.tovarelo.net)
I may want a section on finance as well, not sure at this moment

I want this site to be a personal website, not a subscription service or professional services sales site, I want the site to look very professional, so that I can share it with all types of people without concern - business, spiritual, other.

I have provided a photo of myself for the site, smart casual on a beach. The site will be hosted on brennmorlock.net

You can see samples of what I am referring to by searching "personal website" on images.zumvaro.net

I would like the page layout, and the images chopped up as individual jpgs, including hover images for buttons. I can do the coding

I would like the following buttons
Home, About, Information Security Blog, Passion Projects, Contact

I would like the top portion of the page to say "Dorian Pell"
I would like the subtext to say:
Executive Information Security Architect, Author, and Idea Man

I envision the following

Target Market(s)

Executive / Technical / Creative types / Spritual types

Number of Pages Required

4 page

Requirements
Must have
• Blog section
Should not have
• No Matrix themes or No Cop themes, No Fingerprints or Eyeball scans

```html
<!DOCTYPE html>
<html lang="en">
<head>
<meta charset="utf-8">
<title>Dorian Pell — Information Security Consultant</title>
<link href="https://fonts.googleapis.com/css2?family=Oswald:wght@400;500&family=Roboto:wght@400;500;700&display=swap" rel="stylesheet">
<style>
:root{
  --blue:#2f9be0;
  --blue-dark:#1f86c9;
  --ink:#2e3338;
  --muted:#8a9096;
  --page:#e8ebee;
  --card:#ffffff;
  --line:#dde1e5;
  --footer:#2b8fd6;
  --bottom:#2a2e33;
  --hero-a:#0d5c92;
  --hero-b:#9fd3f2;
}
*{box-sizing:border-box;margin:0;padding:0}
html,body{width:1200px;height:2184px;overflow:hidden}
body{font-family:Roboto,Arial,sans-serif;color:var(--ink);background:var(--page);position:relative;font-size:12px}
.site-header{height:80px;background:#fff;display:flex;align-items:center;justify-content:space-between;padding:0 80px;border-bottom:1px solid var(--line)}
.logo{font-family:Oswald,sans-serif;font-size:30px;font-weight:500;letter-spacing:1px;color:var(--ink)}
.nav{display:flex;gap:22px;align-items:center;font-size:11px;font-weight:500;text-transform:uppercase}
.nav a{color:var(--ink);text-decoration:none}
.nav a.active{color:var(--blue)}
.nav .login{background:var(--blue);color:#fff;padding:6px 14px;border-radius:2px}
.hero{position:absolute;top:80px;left:0;width:1200px;height:620px;background:radial-gradient(circle at 32% 45%,var(--hero-b) 0,#4aa8e0 22%,var(--hero-a) 62%,#08385e 100%)}
.hero-title{position:absolute;right:84px;top:440px;text-align:right;font-family:Oswald,sans-serif;text-transform:uppercase;line-height:1.05}
.hero-title .l1{font-size:38px;color:#fff}
.hero-title .l2{font-size:38px;color:#9fe0ff}
.slider-arrows{position:absolute;right:90px;top:552px;display:flex;gap:2px}
.slider-arrows span{width:20px;height:20px;background:#2c3238;display:flex;align-items:center;justify-content:center}
.main{position:absolute;top:700px;left:0;width:1200px;height:1212px;background:var(--page)}
.section-title{position:absolute;left:88px;top:66px;font-family:Oswald,sans-serif;font-size:18px;text-transform:uppercase;color:var(--ink)}
.section-title b{color:var(--blue);font-weight:400}
.posts{position:absolute;left:88px;top:100px;width:824px}
.post{background:var(--card);height:228px;margin-bottom:24px;display:flex;padding:14px;gap:22px;box-shadow:0 1px 2px rgba(0,0,0,.08)}
.post-thumb{width:240px;height:168px;flex:none}
.post-body{flex:1;padding-top:2px}
.post-title{font-size:15px;color:var(--blue);font-weight:500;margin-bottom:6px}
.post-meta{font-size:11px;color:var(--muted);margin-bottom:12px}
.post-excerpt{font-size:11.5px;line-height:1.6;color:#555b61;margin-bottom:14px}
.post-actions{display:flex;align-items:center;gap:10px}
.btn{background:var(--blue);color:#fff;font-size:10px;font-weight:700;text-transform:uppercase;padding:6px 14px;border-radius:2px}
.share{font-size:10px;border:1px solid var(--line);padding:3px 8px;border-radius:2px;color:var(--muted)}
.sidebar{position:absolute;left:932px;top:100px;width:180px}
.widget{background:var(--card);box-shadow:0 1px 2px rgba(0,0,0,.08);margin-bottom:20px}
.widget-head{background:var(--blue);color:#fff;font-family:Oswald,sans-serif;font-size:14px;text-transform:uppercase;padding:10px 14px}
.popular li{list-style:none;display:flex;gap:10px;padding:12px;border-bottom:1px solid var(--line)}
.popular .thumb{width:52px;height:60px;flex:none;background:linear-gradient(135deg,#6b88a8,#c9a978)}
.popular h4{font-size:11px;font-weight:500;color:var(--ink);margin-bottom:4px}
.popular p{font-size:9.5px;line-height:1.4;color:var(--muted)}
.archives li{list-style:none;font-size:11px;color:var(--ink);padding:11px 16px;border-bottom:1px solid var(--line);display:flex;gap:8px;align-items:center}
.archives li::before{content:"";width:5px;height:5px;border-radius:50%;background:var(--blue)}
.video{height:220px;position:relative;background:linear-gradient(135deg,#0b3b66,#2f90d0 60%,#0c2f52)}
.video .play{position:absolute;left:50%;top:50%;width:52px;height:52px;margin:-26px 0 0 -26px;border-radius:50%;background:rgba(255,255,255,.85);display:flex;align-items:center;justify-content:center}
.pagination{position:absolute;left:88px;top:1138px;display:flex;gap:4px}
.pagination span{background:#fff;border:1px solid var(--line);font-size:10px;min-width:26px;height:24px;padding:0 6px;display:flex;align-items:center;justify-content:center;color:var(--ink)}
.pagination span.current{background:var(--blue);color:#fff;border-color:var(--blue)}
.site-footer{position:absolute;top:1912px;left:0;width:1200px;height:208px;background:var(--footer);color:#fff;display:flex;padding:34px 80px 0 88px;gap:40px}
.footer-col{width:230px}
.footer-col h5{font-family:Oswald,sans-serif;font-size:13px;font-weight:400;text-transform:uppercase;margin-bottom:14px}
.footer-col p,.footer-col li{font-size:10px;line-height:1.6;color:#e3f1fb;list-style:none}
.footer-col li{padding-left:10px;position:relative}
.footer-col li::before{content:"›";position:absolute;left:0}
.subscribe{display:flex;margin:10px 0 14px}
.subscribe span{background:#fff;width:150px;height:24px}
.subscribe b{background:var(--bottom);font-size:10px;padding:0 10px;display:flex;align-items:center;font-weight:500}
.social{display:flex;gap:10px}
.social span{width:26px;height:26px;border-radius:50%;background:#2a7cbd}
.bottom-bar{position:absolute;top:2120px;left:0;width:1200px;height:64px;background:var(--bottom);color:#c4c9ce;font-size:10px;display:flex;align-items:center;justify-content:space-between;padding:0 80px 0 88px}
</style>
</head>
<body>
<header class="site-header">
  <div class="logo">DORIANPELL</div>
  <nav class="nav">
    <a class="active" href="#">Home</a><a href="#">About Us</a><a href="#">Services</a><a href="#">Categories</a><a href="#">Blog</a><a href="#">Contacts</a><a class="login" href="#">Login</a>
  </nav>
</header>

<section class="hero" role="img" aria-label="Blue technology scene with a glowing padlock and network icons">
  <div class="hero-title"><div class="l1">Information Security</div><div class="l2">Consultant</div></div>
  <div class="slider-arrows">
    <span><svg width="8" height="8" viewBox="0 0 8 8"><path d="M6 0L2 4l4 4" stroke="#fff" fill="none" stroke-width="1.5"/></svg></span>
    <span><svg width="8" height="8" viewBox="0 0 8 8"><path d="M2 0l4 4-4 4" stroke="#fff" fill="none" stroke-width="1.5"/></svg></span>
  </div>
</section>

<main class="main">
  <h2 class="section-title">Latest <b>Blog</b></h2>
  <div class="posts">
    <article class="post">
      <div class="post-thumb" role="img" aria-label="Blue padlock on a circuit board" style="background:linear-gradient(135deg,#0f4f7a,#39a3d8)"></div>
      <div class="post-body">
        <h3 class="post-title">Neque porro quisquam est qui dolorem ipsum</h3>
        <div class="post-meta">Post by : admin &nbsp;|&nbsp; Post on : October 1, 2015 &nbsp;at 10:15 p.m.</div>
        <p class="post-excerpt">Sed ut perspiciatis unde omnis iste natus error sit voluptatem accusantium doloremque laudantium, totam rem aperiam eaque ipsa quae ab illo inventore veritatis et quasi architecto beatae vitae dicta sunt explicabo nemo enim.</p>
        <div class="post-actions"><span class="btn">Learn More</span><span class="share">Share</span><span class="share">Like</span><span class="share">+1</span></div>
      </div>
    </article>
    <article class="post">
      <div class="post-thumb" role="img" aria-label="Open book with warm light" style="background:linear-gradient(135deg,#f0d9a8,#b06a2c)"></div>
      <div class="post-body">
        <h3 class="post-title">Neque porro quisquam est qui dolorem ipsum</h3>
        <div class="post-meta">Post by : admin &nbsp;|&nbsp; Post on : October 1, 2015 &nbsp;at 10:15 p.m.</div>
        <p class="post-excerpt">Nemo enim ipsam voluptatem quia voluptas sit aspernatur aut odit aut fugit, sed quia consequuntur magni dolores eos qui ratione voluptatem sequi nesciunt neque porro quisquam est qui dolorem ipsum quia dolor sit amet.</p>
        <div class="post-actions"><span class="btn">Learn More</span><span class="share">Share</span><span class="share">Like</span><span class="share">+1</span></div>
      </div>
    </article>
    <article class="post">
      <div class="post-thumb" role="img" aria-label="Family group outdoors" style="background:linear-gradient(135deg,#8fb26a,#4f6d3a)"></div>
      <div class="post-body">
        <h3 class="post-title">Neque porro quisquam est qui dolorem ipsum</h3>
        <div class="post-meta">Post by : admin &nbsp;|&nbsp; Post on : October 1, 2015 &nbsp;at 10:15 p.m.</div>
        <p class="post-excerpt">Ut enim ad minima veniam, quis nostrum exercitationem ullam corporis suscipit laboriosam, nisi ut aliquid ex ea commodi consequatur quis autem vel eum iure reprehenderit qui in ea voluptate velit esse quam nihil molestiae.</p>
        <div class="post-actions"><span class="btn">Learn More</span><span class="share">Share</span><span class="share">Like</span><span class="share">+1</span></div>
      </div>
    </article>
    <article class="post">
      <div class="post-thumb" role="img" aria-label="Hand touching a digital finance screen" style="background:linear-gradient(135deg,#1c2f4a,#6f8db0)"></div>
      <div class="post-body">
        <h3 class="post-title">Neque porro quisquam est qui dolorem ipsum</h3>
        <div class="post-meta">Post by : admin &nbsp;|&nbsp; Post on : October 1, 2015 &nbsp;at 10:15 p.m.</div>
        <p class="post-excerpt">At vero eos et accusamus et iusto odio dignissimos ducimus qui blanditiis praesentium voluptatum deleniti atque corrupti quos dolores et quas molestias excepturi sint occaecati cupiditate non provident similique sunt.</p>
        <div class="post-actions"><span class="btn">Learn More</span><span class="share">Share</span><span class="share">Like</span><span class="share">+1</span></div>
      </div>
    </article>
  </div>

  <aside class="sidebar">
    <div class="widget">
      <div class="widget-head">Popular Posts</div>
      <ul class="popular">
        <li><div class="thumb" role="img" aria-label="Post thumbnail"></div><div><h4>This is a sample Post 1</h4><p>Lorem ipsum dolor sit amet, consectetur adipiscing elit sed do.</p></div></li>
        <li><div class="thumb" role="img" aria-label="Post thumbnail"></div><div><h4>This is a sample Post 2</h4><p>Lorem ipsum dolor sit amet, consectetur adipiscing elit sed do.</p></div></li>
        <li><div class="thumb" role="img" aria-label="Post thumbnail"></div><div><h4>This is a sample Post 3</h4><p>Lorem ipsum dolor sit amet, consectetur adipiscing elit sed do.</p></div></li>
        <li><div class="thumb" role="img" aria-label="Post thumbnail"></div><div><h4>This is a sample Post 4</h4><p>Lorem ipsum dolor sit amet, consectetur adipiscing elit sed do.</p></div></li>
        <li style="border:0"><div class="thumb" role="img" aria-label="Post thumbnail"></div><div><h4>This is a sample Post 5</h4><p>Lorem ipsum dolor sit amet, consectetur adipiscing elit sed do.</p></div></li>
      </ul>
    </div>
    <div class="widget" style="margin-top:48px">
      <div class="widget-head">Archives</div>
      <ul class="archives">
        <li>April 2015</li><li>March 2015</li><li>February 2015</li><li>January 2015</li><li style="border:0">September 2014</li>
      </ul>
    </div>
    <div class="widget video" role="img" aria-label="Video preview of a digital security scene">
      <div class="play"><svg width="18" height="20" viewBox="0 0 18 20"><path d="M3 1l14 9-14 9z" fill="#1f86c9"/></svg></div>
    </div>
  </aside>

  <div class="pagination"><span>Prev</span><span class="current">1</span><span>2</span><span>3</span><span>4</span><span>5</span><span>…</span><span>10</span><span>Next</span></div>
</main>

<footer class="site-footer">
  <div class="footer-col">
    <h5>Text Widget</h5>
    <p>Vestibulum tempor nisi ut sodales, sed dolor mauris vulputate nibh, sit amet tincidunt lectus.</p>
    <p style="margin-top:8px">Proin gravida nibh vel velit auctor aliquet, aenean sollicitudin lorem quis bibendum auctor nisi elit consequat.</p>
  </div>
  <div class="footer-col">
    <h5>Links</h5>
    <ul><li>Information Security</li><li>Passion Projects</li><li>Enterprise</li><li>Special Policy</li><li>Terms of use</li></ul>
  </div>
  <div class="footer-col">
    <h5>Get in Touch</h5>
    <p>Address : 2840 Harlow Mill Road,<br>North Elvaria, NL</p>
    <p style="margin-top:8px">Phone : 555 014 2283</p>
    <p style="margin-top:8px">Email : info@brennmorlock.net</p>
  </div>
  <div class="footer-col">
    <h5>Newsletter</h5>
    <p>Enter your address to receive our latest updates.</p>
    <div class="subscribe"><span></span><b>Submit</b></div>
    <div class="social"><span></span><span></span><span></span></div>
  </div>
</footer>

<div class="bottom-bar">
  <span>Website Design: Larkfield Studio</span>
  <span>Copyright © 2015. All Rights Reserved</span>
</div>
</body>
</html>
```